Business card design for upmarket Home Technology design and Installation company

Hello designers, we need a great business card designed.
We need it to convey high tech, and also sophistication .
We work with some of the most affluent people in the world building them home technology systems, and A/V entertainment systems.

Services offered include the following:
Design, sales, installation, and maintenance of

*Home Automation systems
*Distributed / Multi-Room Audio and Video
*High Performance Networks & WiFi
* Lighting and Shade Control
*Home cinema
*Security and CCTV Systems

I have included a copy of our logo to use for your design efforts.

Target Market(s)

Upmarket clients with multi million euro villas.

Industry/Entity Type

Home technology

Contact Information for Business Card

NAME: Derek Halvin ADDRESS: Carrer Bellamar Local 42, Cala Torrent, 07293 PHONE: +34-652-918-204 EMAIL: DHalvin@VORTELhomesystems.example WEB: www.vortelhomesystems.example

Requirements
Must have
• Our Logo, and our tagline

```html
<!DOCTYPE html>
<html lang="en">
<head>
<meta charset="utf-8">
<title>VORTEL Business Card</title>
<link rel="stylesheet" href="https://fonts.googleapis.com/css2?family=Poppins:wght@300;400&family=Roboto:wght@300;400;500&display=swap">
<style>
  :root {
    --backdrop: #3a302b;
    --card: #1d1d1e;
    --card-edge: #2a2a2b;
    --gold: #d2ad4e;
    --gold-dark: #a9822a;
    --ink-light: #f2f2f2;
  }
  html, body {
    margin: 0;
    width: 1200px;
    height: 716px;
    overflow: hidden;
    background: var(--backdrop);
  }
  .canvas {
    position: relative;
    width: 1200px;
    height: 716px;
  }
  .card {
    position: absolute;
    top: 204px;
    width: 540px;
    height: 308px;
    background: linear-gradient(135deg, var(--card-edge) 0%, var(--card) 60%);
    box-shadow: 0 10px 28px rgba(0,0,0,.45);
    overflow: hidden;
  }
  .card--front { left: 40px; }
  .card--back { left: 620px; }

  /* Front */
  .front-brand {
    position: absolute;
    left: 52px;
    top: 96px;
    width: 260px;
    text-align: center;
  }
  .brand-name {
    font-family: "Roboto", sans-serif;
    font-weight: 300;
    color: var(--gold);
    letter-spacing: .18em;
    margin: 0;
    line-height: 1;
  }
  .front-brand .brand-name { font-size: 52px; }
  .tagline-rule {
    display: flex;
    align-items: center;
    gap: 8px;
    margin-top: 10px;
  }
  .tagline-rule::before,
  .tagline-rule::after {
    content: "";
    flex: 1;
    height: 1px;
    background: var(--gold-dark);
  }
  .tagline {
    font-family: "Poppins", sans-serif;
    font-weight: 300;
    font-size: 11px;
    letter-spacing: .28em;
    color: var(--gold);
  }
  .front-bar {
    position: absolute;
    right: 20px;
    top: 0;
    width: 9px;
    height: 58px;
    background: linear-gradient(180deg, var(--gold), var(--gold-dark));
  }

  /* Back */
  .back-brand {
    position: absolute;
    right: 34px;
    top: 62px;
  }
  .back-brand .brand-name { font-size: 36px; }
  .contact {
    position: absolute;
    right: 34px;
    top: 140px;
    text-align: right;
    font-family: "Roboto", sans-serif;
  }
  .contact-name {
    margin: 0;
    font-weight: 500;
    font-size: 22px;
    letter-spacing: .04em;
    color: var(--gold);
    text-transform: uppercase;
  }
  .contact-title {
    margin: 0 0 8px;
    font-weight: 400;
    font-size: 12px;
    letter-spacing: .08em;
    color: var(--ink-light);
  }
  .contact-lines {
    list-style: none;
    margin: 0;
    padding: 0;
    font-size: 12.5px;
    line-height: 18px;
    color: var(--ink-light);
  }
  .contact-lines li {
    display: flex;
    justify-content: flex-end;
    align-items: center;
    gap: 6px;
  }
  .contact-lines svg {
    width: 10px;
    height: 10px;
    flex: none;
  }
  .icon-space { display: inline-block; width: 10px; }
  .back-bar {
    position: absolute;
    right: 0;
    top: 190px;
    width: 7px;
    height: 40px;
    background: linear-gradient(180deg, var(--gold), var(--gold-dark));
  }
  .back-bar--top {
    left: 92px;
    right: auto;
    top: 0;
    width: 9px;
    height: 58px;
  }
</style>
</head>
<body>
<main class="canvas">

  <section class="card card--front" aria-label="Card front">
    <div class="front-brand">
      <p class="brand-name">VORTEL</p>
      <div class="tagline-rule"><span class="tagline">SMARTER HOMES</span></div>
    </div>
    <div class="front-bar"></div>
  </section>

  <section class="card card--back" aria-label="Card back">
    <div class="back-bar back-bar--top"></div>
    <div class="back-brand">
      <p class="brand-name">VORTEL</p>
    </div>
    <div class="contact">
      <p class="contact-name">Derek Halvin</p>
      <p class="contact-title">DIRECTOR</p>
      <ul class="contact-lines">
        <li>Carrer Bellamar Local 42,<span class="icon-space"></span></li>
        <li>Cala Torrent, 07293<span class="icon-space"></span></li>
        <li>+34-652-918-204
          <svg viewBox="0 0 10 10" aria-hidden="true"><path d="M2 1 L4 1 L4.6 3 L3.4 3.8 Q4.4 5.8 6.2 6.6 L7 5.4 L9 6 L9 8 Q8 9.2 6.5 8.8 Q2.2 7.4 1.2 3 Q1 1.8 2 1Z" fill="var(--gold)"/></svg>
        </li>
        <li>DHalvin@VORTELhomesystems.example
          <svg viewBox="0 0 10 10" aria-hidden="true"><rect x="0.8" y="2" width="8.4" height="6" fill="none" stroke="var(--gold)" stroke-width="1"/><path d="M0.8 2 L5 5.4 L9.2 2" fill="none" stroke="var(--gold)" stroke-width="1"/></svg>
        </li>
        <li>www.vortelhomesystems.example
          <svg viewBox="0 0 10 10" aria-hidden="true"><circle cx="5" cy="5" r="4.2" fill="none" stroke="var(--gold)" stroke-width="1"/><ellipse cx="5" cy="5" rx="1.8" ry="4.2" fill="none" stroke="var(--gold)" stroke-width=".8"/><path d="M0.8 5 H9.2" stroke="var(--gold)" stroke-width=".8"/></svg>
        </li>
      </ul>
    </div>
    <div class="back-bar"></div>
  </section>

</main>
</body>
</html>
```